Harbor Relay Group Letterhead Design

The project name sums it up. Just need a professional letterhead design / template we can use in our marketing folders.

Here's the address / contact info for the letterhead: Harbor Relay Group 4815 Maple Crest Ave Suite 210 Cedar Hollow, Oregon 77419 555-507-3846 www.harborrelaygroup.us support@harborrelaygroup.us

```html
<!DOCTYPE html>
<html lang="en">
<head>
<meta charset="utf-8">
<title>Harbor Relay Group Letterhead</title>
<link href="https://fonts.googleapis.com/css2?family=Roboto:wght@300;400;700&family=Pinyon+Script&display=swap" rel="stylesheet">
<style>
  :root {
    --backdrop: #e4e4e4;
    --paper: #f5f5f5;
    --paper-shade: #ececec;
    --ink: #222222;
    --ink-soft: #6b6b6b;
    --brand-blue: #134c9c;
    --rule: #9a9a9a;
  }
  * { margin: 0; padding: 0; box-sizing: border-box; }
  html, body {
    width: 1200px; height: 1200px; overflow: hidden;
    background: var(--backdrop);
    font-family: "Roboto", Arial, sans-serif;
  }
  .letterhead {
    position: absolute; left: 196px; top: 30px;
    width: 807px; height: 1140px;
    background: linear-gradient(160deg, #fafafa 0%, var(--paper) 45%, var(--paper-shade) 100%);
    box-shadow: 0 6px 22px rgba(0,0,0,0.12);
    overflow: hidden;
  }
  .brand {
    position: absolute; left: 52px; top: 86px;
    display: flex; align-items: center; gap: 10px;
  }
  .brand-mark { width: 22px; height: 22px; background: var(--brand-blue); }
  .brand-name {
    font-weight: 700; font-size: 22px; color: var(--ink); letter-spacing: 0.2px;
  }
  .address {
    position: absolute; left: 353px; top: 76px;
    font-size: 13.5px; line-height: 16.5px; color: var(--ink-soft); font-weight: 400;
    font-style: normal;
  }
  .divider {
    position: absolute; left: 506px; top: 78px;
    width: 1px; height: 44px; background: var(--rule);
  }
  .contacts {
    position: absolute; left: 531px; top: 76px;
    list-style: none; font-size: 13.5px; line-height: 16.5px; color: var(--ink-soft);
  }
  .contacts li { display: flex; align-items: center; gap: 6px; }
  .contacts svg { width: 10px; height: 10px; flex: none; }
  .letter {
    position: absolute; left: 86px; top: 268px; width: 635px;
    font-size: 13.6px; line-height: 19px; color: var(--ink); font-weight: 300;
    letter-spacing: 0.05px;
  }
  .letter .date { margin-bottom: 19px; }
  .letter .recipient { margin-bottom: 38px; }
  .letter .salutation { margin-bottom: 19px; }
  .letter .body p { text-align: justify; margin-bottom: 19px; }
  .closing { margin-top: 55px; }
  .signature {
    font-family: "Pinyon Script", cursive;
    font-size: 30px; line-height: 40px; margin-top: 4px; color: var(--ink);
  }
  .footer-band { position: absolute; left: 0; bottom: 0; width: 807px; height: 28px; }
</style>
</head>
<body>
  <main class="letterhead">
    <header>
      <div class="brand">
        <span class="brand-mark"></span>
        <span class="brand-name">Harbor Relay Group</span>
      </div>
      <address class="address">
        4815 Maple Crest Ave.<br>
        Suite 210 Cedar Hollow<br>
        Oregon 77419
      </address>
      <div class="divider"></div>
      <ul class="contacts">
        <li>
          <svg viewBox="0 0 10 10"><path d="M2 0.5 L3.6 2.6 L2.8 3.6 Q4 5.9 6.4 7.2 L7.4 6.4 L9.5 8 L8.3 9.5 Q4.5 9.2 1.8 6.4 Q0.4 4.2 0.5 1.8 Z" fill="var(--brand-blue)"/></svg>
          555-507-3846
        </li>
        <li>
          <svg viewBox="0 0 10 10"><rect x="0.7" y="1.8" width="8.6" height="6.4" fill="none" stroke="var(--brand-blue)" stroke-width="1"/><path d="M0.7 1.8 L5 5.5 L9.3 1.8" fill="none" stroke="var(--brand-blue)" stroke-width="1"/></svg>
          support@harborrelaygroup.us
        </li>
        <li>
          <svg viewBox="0 0 10 10"><circle cx="5" cy="5" r="4.3" fill="none" stroke="var(--brand-blue)" stroke-width="1"/><ellipse cx="5" cy="5" rx="1.8" ry="4.3" fill="none" stroke="var(--brand-blue)" stroke-width="0.9"/><path d="M0.7 5 H9.3" stroke="var(--brand-blue)" stroke-width="0.9"/></svg>
          www.harborrelaygroup.us
        </li>
      </ul>
    </header>

    <section class="letter">
      <p class="date">01 January 2050</p>
      <p class="recipient">Company (Pvt) Ltd.<br>PO Box 3355 Mainville St<br>Sample City Country 3355</p>
      <p class="salutation">Dear Daniel Whitcombe,</p>
      <div class="body">
        <p>Lorem ipsum dolor sit amet, consectetuer adipiscing elit, sed diam nonummy nibh euismod tincidunt ut laoreet dolore magna aliquam erat volutpat. Ut wisi enim ad minim veniam, quis nostrud exerci tation ullamcorper suscipit lobortis nisl ut aliquip ex ea commodo consequat. Duis dolore te feugait nulla facilisi. Nam liber tempor cum soluta nobis eleifend option congue nihil imperdiet doming id quod mazim placerat facer possim assum. Lorem ipsum dolor sit amet, consectetuer adipiscing elit, sed diam nonummy nibh euismod tincidunt ut laoreet dolore magna aliquam erat volutpat. Ut wisi enim ad minim veniam, quis nostrud exerci tation ullamcorper suscipit lobortis nisl ut aliquip ex ea commodo consequat.</p>
        <p>Consectetuer adipiscing elit, sed diam nonummy nibh euismod tincidunt ut laoreet dolore magna aliquam erat volutpat. Ut wisi enim ad minim veniam, quis nostrud exerci tation ullamcorper suscipit lobortis nisl ut aliquip ex ea commodo consequat. Consectetuer adipiscing elit, sed diam nonummy nibh euismod tincidunt ut laoreet dolore magna aliquam erat volutpat. Ut wisi enim ad minim veniam, quis nostrud exerci tation ullamcorper suscipit lobortis nisl ut aliquip ex ea commodo consequat.</p>
        <p>Consectetuer adipiscing elit, sed diam nonummy nibh euismod tincidunt ut laoreet dolore magna aliquam erat volutpat. Ut wisi enim ad minim veniam, quis nostrud exerci tation ullamcorper suscipit lobortis nisl ut aliquip ex ea commodo consequat. Consectetuer adipiscing elit, sed diam nonummy nibh euismod tincidunt ut laoreet dolore magna aliquam erat volutpat. Ut wisi enim ad minim veniam, quis nostrud exerci tation ullamcorper suscipit lobortis nisl ut aliquip ex ea commodo consequat.</p>
      </div>
      <p class="closing">Sincerely Yours</p>
      <p class="signature">Thomas Arnell</p>
    </section>

    <svg class="footer-band" viewBox="0 0 807 28" preserveAspectRatio="none">
      <defs>
        <linearGradient id="steel" x1="0" x2="1" y1="0" y2="0">
          <stop offset="0" stop-color="#6f6f6f"/>
          <stop offset="0.5" stop-color="#c4c4c4"/>
          <stop offset="1" stop-color="#5e5e5e"/>
        </linearGradient>
      </defs>
      <polygon points="0,15 502,15 495,28 0,28" fill="url(#steel)"/>
      <polygon points="512,0 807,0 807,28 498,28" fill="var(--brand-blue)"/>
    </svg>
  </main>
</body>
</html>
```